New Web Page Design - Cement Rendering Business

Looking for a overhaul of our existing website (www.olpa.com.au).

Looking for a sleek and elegant design that incorporates the colours of our logos, black / green and white. Needs to look professional and want it to be well above what our competition is offering. (Zorbix search for 'cement rendering sydney' will display the competition we want to be well ahead of.

Prefer a mixture of pages with black background and white alternatively between home (black), about us (white), contact us (black) and gallery (white).

Would like to incorporate our logo on all pages attached preferably in the top left corner.

Website needs to be search engine optimised and have easily updated photo gallery which we already have.

Also need to embed our zorbix metrics code on the front home page.

Website needs to be able easily updated (text, pictures ) as required.
content management system should include fields where you can alter your page titles, meta description and keywords.

Pages also needs to be optimised for mobile devices, kelphone, kelpad and other mobile devices. (it is a current feature we have)

If you have any questions, just message me.

Please remember the look and feel of the site is important to us, we don't want it over complicated, simple elegant and professional in line with our logo standards.
Updates

Hi All, As an example of the look and feel we like. We have found a site that may assist in your design and creative process. http://beta.marvodesk.org/ We like the simplicity, elegance and professional look of this site, although we would like it with our images, colours and logos. I hope this helps.! keep the great designs coming!

All, Thanks for the designs. Please try and use our website images due to copyright reasons for all your designs. Boris

Target Market(s)

Construction Companies

Industry/Entity Type

Business

Colors
9bcb3b
acd036
474747

Requirements
Must have
• Search Engine Optimised.
Photo Gallery
Elegant/Professional Look & Feel.
Simple Yet Effective
Nice to have
• Moving Parts
Should not have
• Overly Complicated.
Cheap & Traditional Looking.
Boring

```html
<!DOCTYPE html>
<html lang="en">
<head>
<meta charset="utf-8">
<title>OLPA Cement Rendering</title>
<link href="https://fonts.googleapis.com/css2?family=Comfortaa:wght@300;400;700&family=Open+Sans:wght@400;600&display=swap" rel="stylesheet">
<style>
:root{
  --black:#111111;
  --green:#9bcb3b;
  --green-band:#95bf46;
  --grey-dark:#474747;
  --paper:#ebebeb;
  --white:#ffffff;
  --text:#222222;
  --muted:#cfcfcf;
}
*{margin:0;padding:0;box-sizing:border-box}
html,body{width:1200px;height:2413px;overflow:hidden}
body{position:relative;background:var(--white);font-family:"Open Sans",Arial,sans-serif;color:var(--text)}
.abs{position:absolute}
.display{font-family:"Comfortaa",sans-serif}

.site-header{left:0;top:0;width:1200px;height:121px;background:var(--black)}
.brand{left:154px;top:30px;height:60px;line-height:60px;font-family:"Open Sans",sans-serif;font-size:38px;font-weight:400;color:var(--white);letter-spacing:2px}
.main-nav a{position:absolute;top:53px;height:31px;line-height:31px;font-family:"Comfortaa",sans-serif;font-size:16px;color:var(--white);text-decoration:none}
.main-nav .active{left:536px;width:77px;text-align:center;background:var(--green);border-radius:3px}

.hero{left:0;top:121px;width:1200px;height:503px;background:linear-gradient(100deg,#5a4e48 0%,#6e6e6e 30%,#8a8a8a 60%,#7a7a7a 100%)}
.hero-title{left:0;top:200px;width:1200px;text-align:center;font-size:50px;font-weight:700;color:var(--green)}
.hero-sub{left:0;top:264px;width:1200px;text-align:center;font-size:27px;font-weight:400;color:var(--white)}
.hero-screen{left:338px;top:327px;width:500px;height:297px;border-radius:14px 14px 0 0;background:linear-gradient(135deg,#3a3a3a,#5c5c5c 60%,#c9772f)}

.section-title{left:0;width:1200px;text-align:center;font-size:48px;font-weight:300;color:var(--black)}
.about-title{top:700px}
.about-photo{left:143px;top:799px;width:299px;height:267px;border:7px solid #b5d86c;background:linear-gradient(135deg,#c96a3a,#9a9a9a 45%,#cfcfcf)}
.about-copy{left:458px;top:800px;width:592px;font-size:12.4px;line-height:18.5px}
.about-copy p{margin-bottom:17px}

.gallery{left:0;top:1150px;width:1200px;height:471px;background:var(--green-band)}
.gallery-title{top:1176px;padding-right:24px}
.thumb{width:204px;height:204px;top:1298px;border-radius:50%;border:3px solid #dfe9cf}
.arrow{top:1370px}

.contact{left:0;top:1621px;width:1200px;height:682px;background:var(--paper)}
.contact-title{top:1654px;padding-right:40px}
.field{left:153px;width:349px;height:31px;background:var(--white);border:1px solid #b9b9b9;border-radius:3px;font-size:13px;color:#9a9a9a;padding:6px 10px;font-family:Arial,sans-serif}
.captcha{left:153px;top:2128px;width:148px;height:55px;background:linear-gradient(90deg,#111,#444,#111)}
.code-label{left:315px;top:2132px;font-size:13px;color:#9a9a9a;font-family:Arial,sans-serif}
.code-input{left:314px;top:2156px;width:109px;height:28px;background:var(--white);border:1px solid #b9b9b9;border-radius:3px}
.send{left:153px;top:2215px;width:101px;height:35px;background:var(--green);border-radius:3px;text-align:center;line-height:35px;font-family:"Comfortaa",sans-serif;font-size:17px;color:var(--black)}
.map-frame{left:589px;top:1758px;width:441px;height:336px;background:var(--white);border:1px solid #c9c9c9;padding:10px}
.map{width:100%;height:100%;background:linear-gradient(135deg,#e9dfb8,#f1ead0 45%,#a9c9ef 70%)}
.contact-info{left:589px;top:2124px;font-family:Arial,sans-serif;font-size:13.5px;line-height:24px;color:#333}

.site-footer{left:0;top:2303px;width:1200px;height:110px;background:var(--black)}
.footer-text{color:var(--white);font-family:Arial,sans-serif;font-size:12px}
.footer-left{left:151px;top:2329px;line-height:19px}
.footer-nav{left:0;top:2336px;width:1200px;text-align:center;padding-left:40px}
.footer-nav span{margin:0 8px}
.copyright{left:0;top:2362px;width:1200px;text-align:center;padding-left:40px}
.footer-brand{left:940px;top:2334px;height:44px;line-height:44px;font-family:"Open Sans",sans-serif;font-size:30px;font-weight:400;color:var(--muted);letter-spacing:2px}
</style>
</head>
<body>

<header class="abs site-header"></header>
<div class="abs brand">OLPA</div>
<nav class="main-nav">
  <a class="active">Home</a>
  <a style="left:666px">About Us</a>
  <a style="left:804px">Photo Gallery</a>
  <a style="left:978px">Contact Us</a>
</nav>

<section class="abs hero" role="img" aria-label="Photo of a gloved hand rendering a cement wall"></section>
<h1 class="abs hero-title display">25 years of experience</h1>
<p class="abs hero-sub display">OLPA Cement Rendering</p>
<div class="abs hero-screen" role="img" aria-label="Laptop showing a close-up of cement rendering work"></div>

<h2 class="abs section-title about-title display">About Us</h2>
<div class="abs about-photo" role="img" aria-label="Worker smoothing render with a trowel"></div>
<div class="abs about-copy">
  <p>Welcome to OLPA, your one stop shop for all your cement rendering needs.</p>
  <p>We are an Australian owned and operated business with over 25 years of experience in our field.</p>
  <p>Our work is fully licensed, our employee's are trained to the highest standards and all of our work is covered by warranty.</p>
  <p>We offer an obligation free on-site consultation and quotation service for your convenience 7 days per week.</p>
  <p>We are the preferred supplier for many of the top building companies in Australia which gives you the access to our expertise, competetive rates and peace of mind.</p>
  <p>No job is too big or too small. We work on several residential, private and commercial projects all year round.</p>
</div>

<section class="abs gallery"></section>
<h2 class="abs section-title gallery-title display">Photo Gallery</h2>
<svg class="abs arrow" style="left:70px" width="30" height="56" viewBox="0 0 30 56"><polyline points="26,4 4,28 26,52" fill="none" stroke="#fff" stroke-width="4"/></svg>
<div class="abs thumb" style="left:138px;background:linear-gradient(135deg,#9a9a9a,#d87a45)" role="img" aria-label="Render being applied by hand"></div>
<div class="abs thumb" style="left:377px;background:linear-gradient(135deg,#2f3338,#5b6068)" role="img" aria-label="Company work van"></div>
<svg class="abs" style="left:454px;top:1374px" width="54" height="54" viewBox="0 0 54 54"><circle cx="22" cy="22" r="15" fill="none" stroke="#9bcb3b" stroke-width="6"/><line x1="33" y1="33" x2="48" y2="48" stroke="#9bcb3b" stroke-width="7" stroke-linecap="round"/></svg>
<div class="abs thumb" style="left:620px;background:linear-gradient(135deg,#6d6d6d,#b9c84a 60%,#3a3a3a)" role="img" aria-label="Renderer in hi-vis shirt at work"></div>
<div class="abs thumb" style="left:858px;background:linear-gradient(180deg,#3f6fb8,#d9d9d9 50%,#6b4a3a)" role="img" aria-label="Rendered building exterior"></div>
<svg class="abs arrow" style="left:1108px" width="30" height="56" viewBox="0 0 30 56"><polyline points="4,4 26,28 4,52" fill="none" stroke="#fff" stroke-width="4"/></svg>

<section class="abs contact"></section>
<h2 class="abs section-title contact-title display">Contact Us</h2>
<div class="abs field" style="top:1763px">Your Name*</div>
<div class="abs field" style="top:1829px">Subject*</div>
<div class="abs field" style="top:1892px">Phone*</div>
<div class="abs field" style="top:1951px">Email*</div>
<div class="abs field" style="top:2019px;height:72px">Your Message*</div>
<div class="abs captcha" role="img" aria-label="Security code image"></div>
<div class="abs code-label">Enter Code*</div>
<div class="abs code-input"></div>
<div class="abs send">SEND</div>
<div class="abs map-frame"><div class="map" role="img" aria-label="Street map showing the business location"></div></div>
<div class="abs contact-info">
  OLPA Cement Rendering<br>
  Phone: (02) 9000 4187<br>
  Mobile: 0400 318 562<br>
  Email: works@olpa.com.au<br>
  Fax: (02) 9000 7731<br>
  Web: www.olpa.com.au
</div>

<footer class="abs site-footer"></footer>
<div class="abs footer-text footer-left">OLPA Cement Rendering<br>ABN: 123 456 789 01<br>www.olpa.com.au</div>
<div class="abs footer-text footer-nav">Home<span>~</span>About Us<span>~</span>Photo Gallery<span>~</span>Contact Us</div>
<div class="abs footer-text copyright">Copyright © 2014 OLPA Cement Rendering. All Rights Reserved.</div>
<div class="abs footer-brand">OLPA</div>

</body>
</html>
```